Need a design package for hair towels wrap

We need package design for hair towel wrap ( 3 pack) brand name is The Vostra. We are looking for simple, contemporary and unique design, color palette 2-3 colors. Paper Box size is 9*8*3 inches with PVC window.Actual picture of the product won't be on the package.Attached Brand Logo and description for the package. Barcode needed to be included on the design package.It will be provided later. Attached sample of the box from manufacturer, and instruction for towel wrap which idea I like, if you could make something similar to it, would be great.

Target Market(s)

Kestrel

Industry/Entity Type

Hair

Colors
848484
f5f5f5
faa54b
333333

Requirements
Must have
• Clean, contemporary design.

```html
<!DOCTYPE html>
<html lang="en">
<head>
<meta charset="utf-8">
<title>The Vostra – Microfiber Hair Towel Wrap Box</title>
<link rel="stylesheet" href="https://fonts.googleapis.com/css2?family=Lato:wght@300;400;700;900&display=swap">
<style>
  :root {
    --grey: #848484;
    --paper: #f5f5f5;
    --orange: #faa54b;
    --ink: #333333;
    --stage: #e4e4e4;
  }
  * { box-sizing: border-box; margin: 0; padding: 0; }
  html, body { width: 1200px; height: 900px; overflow: hidden; }
  body {
    background: var(--stage);
    font-family: "Lato", sans-serif;
    color: var(--ink);
    position: relative;
  }
  .dieline {
    position: absolute;
    left: 240px; top: 120px;
    width: 720px; height: 660px;
  }
  .panel {
    position: absolute;
    background: var(--paper);
    overflow: hidden;
  }
  .line-pattern {
    position: absolute; inset: 0;
    background:
      radial-gradient(circle at 50% 62%, rgba(250,165,75,0) 0 28%, rgba(250,165,75,0.16) 29%, rgba(250,165,75,0.08) 60%, rgba(250,165,75,0.03) 100%);
  }
  /* top panel */
  .panel--top { left: 180px; top: 0; width: 540px; height: 180px; border-bottom: 1px solid #ddd; }
  .panel--top .brand { position: absolute; left: 0; right: 0; top: 70px; text-align: center; }
  /* side panel */
  .panel--side { left: 0; top: 180px; width: 180px; height: 480px; border-right: 1px solid #ddd; padding: 40px 18px 0 22px; }
  /* front panel */
  .panel--front { left: 180px; top: 180px; width: 540px; height: 480px; }

  .brand {
    font-weight: 900;
    font-size: 20px;
    letter-spacing: 1.5px;
    text-transform: uppercase;
    color: var(--ink);
  }
  .brand-mark {
    display: inline-block;
    width: 14px; height: 14px;
    background: var(--orange);
    margin-right: 8px;
    vertical-align: -1px;
  }

  .feature-list { list-style: none; position: relative; }
  .feature-list li {
    position: relative;
    padding-left: 16px;
    font-size: 11px;
    line-height: 1.45;
    color: var(--grey);
    margin-bottom: 18px;
  }
  .feature-list li::before {
    content: "";
    position: absolute; left: 0; top: 4px;
    width: 7px; height: 7px;
    border-radius: 50%;
    background: var(--orange);
  }
  .care-symbols { position: absolute; left: 22px; bottom: 40px; display: flex; gap: 8px; }
  .care-symbols span { width: 18px; height: 18px; border: 1.5px solid var(--grey); }

  .window {
    position: absolute;
    left: 115px; top: 110px;
    width: 310px; height: 310px;
    border-radius: 50%;
    border: 6px solid var(--orange);
    background: radial-gradient(circle at 45% 40%, #f4f4f2, #d9d9d6 70%, #c4c4c0);
  }
  .label {
    position: absolute;
    left: 70px; right: 70px; top: 190px;
    text-align: center;
  }
  .label .brand { font-size: 19px; margin-bottom: 8px; }
  .product-title {
    font-weight: 300;
    font-size: 34px;
    line-height: 1.02;
    text-transform: uppercase;
    color: var(--ink);
    letter-spacing: 0.5px;
  }
  .pack-count {
    display: flex; align-items: center; gap: 10px;
    margin-top: 8px;
    font-weight: 700; font-size: 14px;
    color: var(--orange);
    text-transform: uppercase;
    letter-spacing: 0.5px;
  }
  .pack-count::before, .pack-count::after {
    content: ""; flex: 1; height: 1.5px; background: var(--orange);
  }
  .tagline {
    margin-top: 6px;
    font-size: 13px; line-height: 1.35;
    color: var(--ink);
  }
</style>
</head>
<body>
  <div class="dieline">
    <section class="panel panel--top">
      <div class="line-pattern" role="img" aria-label="Fine orange concentric line pattern"></div>
      <div class="brand"><span class="brand-mark"></span>The Vostra</div>
    </section>

    <section class="panel panel--side">
      <div class="line-pattern" role="img" aria-label="Fine orange concentric line pattern"></div>
      <ul class="feature-list">
        <li>Fits all head sizes.</li>
        <li>Suitable for all hair types and lengths. Holds extra long hair.</li>
        <li>Absorbs approximately 75% of the water within 10 min.</li>
        <li>Less time blow-drying means healthier hair.</li>
        <li>Reduces risk of split ends, breakage and frizz.</li>
      </ul>
      <div class="care-symbols"><span></span><span></span><span></span><span></span></div>
    </section>

    <section class="panel panel--front">
      <div class="line-pattern" role="img" aria-label="Fine orange concentric line pattern radiating from the window"></div>
      <div class="window" role="img" aria-label="Window showing the folded white hair towels"></div>
      <div class="label">
        <div class="brand">The Vostra</div>
        <h1 class="product-title">Microfiber Hair<br>Towel Wrap</h1>
        <div class="pack-count">Set of 3 hair towels</div>
        <p class="tagline">The softest, ultra-absorbent,<br>light &amp; safest towel for your beautiful hair</p>
      </div>
    </section>
  </div>
</body>
</html>
```